Healthcare Technology Company Business Card Design

Hi,

We require a new business card design thats catchy and professional.
Our target audience is healthcare professionals. See supplied artwork for our logo.

If you think its achievable please try add the tag line, not necessary however.
"Developing technologies to improve patient care and release operation benefits"

We'll require the following information on the card. No need to have the subject titles but i've referenced them for your convenience.

Personal Details
Mark Towler
Position: Director
Phone Number - 03 9471 5382
Mobile Number - 0427 836 259
Email: firstname.lastname@velkarin.com.au

Company Details
Suite 38, 216 Wendrell Street
Port Melbourne, Victoria
Fax: 03 8214 3975
velkarin.com.au

Prefer a thinner design than the normal stock standard business card dimensions.
Please ensure there is adequate bleed.

Target Market(s)

Healthcare Professionals

Industry/Entity Type

Healthcare

Font styles to use
Sans Serif

Requirements
Must have
• Clean, Sharp Looks
Should not have
• Any healthcare symbols

```html
<!DOCTYPE html>
<html lang="en">
<head>
<meta charset="utf-8">
<title>Velkarin Business Card</title>
<link rel="stylesheet" href="https://fonts.googleapis.com/css2?family=Open+Sans:wght@400;600;700&display=swap">
<style>
  :root {
    --orange: #f3952f;
    --blue: #36688e;
    --navy: #24506a;
    --white: #ffffff;
    --backdrop: #e9e9ee;
  }
  * { box-sizing: border-box; margin: 0; padding: 0; }
  html, body {
    width: 1200px; height: 987px; overflow: hidden;
    background: var(--backdrop);
    font-family: "Open Sans", Arial, sans-serif;
  }
  .canvas {
    position: relative; width: 1200px; height: 987px;
  }
  .card {
    position: absolute; left: 120px; width: 960px; height: 400px;
    border-radius: 28px; overflow: hidden;
    box-shadow: 0 6px 18px rgba(0,0,0,0.12);
  }
  .card--back { top: 50px; background: var(--orange); }
  .card--front { top: 520px; background: var(--white); }

  /* back */
  .back-brand {
    position: absolute; left: 0; right: 0; top: 120px;
    display: flex; align-items: center; justify-content: center; gap: 24px;
  }
  .back-brand__dot {
    width: 54px; height: 54px; border-radius: 50%; background: var(--navy);
  }
  .back-brand__name {
    font-size: 96px; font-weight: 700; color: var(--navy); letter-spacing: -1px; line-height: 1;
  }
  .back-web {
    position: absolute; left: 0; right: 0; bottom: 70px; text-align: center;
    color: var(--white); font-size: 24px; letter-spacing: 7px;
  }

  /* front */
  .front-brand {
    position: absolute; right: 90px; top: 22px;
    display: flex; align-items: center; gap: 18px;
  }
  .front-brand__dot { width: 40px; height: 40px; border-radius: 50%; background: var(--orange); }
  .front-brand__name {
    font-size: 76px; font-weight: 700; color: var(--blue); letter-spacing: -1px; line-height: 1;
  }
  .rule { position: absolute; left: 0; right: 0; height: 2px; background: var(--blue); }
  .rule--top { top: 132px; }
  .rule--bottom { top: 332px; }
  .band {
    position: absolute; left: 0; right: 0; top: 136px; height: 186px;
    background: var(--orange); color: var(--white);
  }
  .address {
    position: absolute; right: 620px; top: 28px; text-align: right;
    font-size: 21px; line-height: 31px;
  }
  .divider {
    position: absolute; left: 360px; top: 26px; width: 1px; height: 130px;
    background: rgba(255,255,255,0.7);
  }
  .contacts { position: absolute; left: 384px; top: 22px; list-style: none; }
  .contacts li {
    display: flex; align-items: center; gap: 12px;
    font-size: 21px; line-height: 34px;
  }
  .contacts svg { width: 20px; height: 20px; flex: none; }
  .person {
    position: absolute; left: 60px; top: 346px; font-size: 26px; line-height: 40px;
  }
  .person__name { color: var(--orange); font-weight: 700; }
  .person__role { color: var(--blue); font-weight: 400; }
</style>
</head>
<body>
<main class="canvas">

  <section class="card card--back" aria-label="Card back">
    <div class="back-brand">
      <span class="back-brand__dot"></span>
      <span class="back-brand__name">Velkarin</span>
    </div>
    <p class="back-web">www.velkarin.com.au</p>
  </section>

  <section class="card card--front" aria-label="Card front">
    <div class="front-brand">
      <span class="front-brand__dot"></span>
      <span class="front-brand__name">Velkarin</span>
    </div>
    <div class="rule rule--top"></div>
    <div class="band">
      <p class="address">Suite 38, 216 Wendrell Street<br>Port Melbourne<br>Victoria</p>
      <div class="divider"></div>
      <ul class="contacts">
        <li>
          <svg viewBox="0 0 20 20"><circle cx="10" cy="10" r="9" fill="none" stroke="#fff" stroke-width="1.6"/><path d="M6.5 5.5l2 0 .8 2.4-1.3 1c.6 1.3 1.6 2.3 2.9 2.9l1-1.3 2.4.8v2c-5 .3-8.1-2.8-7.8-7.8z" fill="#fff"/></svg>
          03 9471 5382
        </li>
        <li>
          <svg viewBox="0 0 20 20"><rect x="6" y="2" width="8" height="16" rx="1.5" fill="#fff"/><rect x="7.5" y="4" width="5" height="8" fill="#f3952f"/></svg>
          0427 836 259
        </li>
        <li>
          <svg viewBox="0 0 20 20"><rect x="2" y="8" width="16" height="9" rx="1.5" fill="#fff"/><rect x="5" y="3" width="10" height="6" fill="#fff"/><rect x="6" y="11" width="8" height="2" fill="#f3952f"/></svg>
          03 8214 3975
        </li>
        <li>
          <svg viewBox="0 0 20 20"><circle cx="10" cy="10" r="9" fill="#fff"/><rect x="5" y="6.5" width="10" height="7" fill="#f3952f"/><path d="M5 6.5l5 4 5-4" fill="none" stroke="#fff" stroke-width="1.2"/></svg>
          firstname.lastname@velkarin.com.au
        </li>
      </ul>
    </div>
    <div class="rule rule--bottom"></div>
    <p class="person"><span class="person__name">Mark Towler,</span> <span class="person__role">Director</span></p>
  </section>

</main>
</body>
</html>
```